Fresh & Clean *NEW* BUSINESS CARD Needed - OPTOMETRY Clinic/Optical

High-tech optometry practice with 3 doctors seeking new business card.  We provide eye exams, sell, designer glasses/contacts/specialty eyewear and treat ocular diseases.  For our business cards, we are seeking fresh, clean, and crisp design as we grow our team (staffing change).  Simply adding doctors is making the card look busy/cluttered.
 Looking for professional, less cluttered look yet still have our logo, doctor names, phone, address, and website....If possible!  :)
Names:
Marcia Trelford, O.D.
Ned Pallister, O.D.
Oona Ferrant, O.D.
Phone: 555-014-2738
Website: www.BrightLensHub.example
Address:  417 Garnet R. Holloway, Maple Hollow, NS 00000
Ultimately we have the main business card with all doctor sames and that card has two versions  (front is always the same).  The back has two designs (1) displays next appointment time/date, (2) for "general use" (non-appointment.)    I have attached what we have used in the past.  
We also need a design template for each team member in our practice with their name, title, and email.   Those should be designed with the "general use" back (see attached).
**Open to entirely new design so don't feel obligated to keep current format.  Need new perspective!  Also including our watermark and some other design features we have consistently used in past in our portfolio.  Included are two options for logos--vertical and horizontal.
**I also would like to remove "Member of Sight Alliance" on our logo if possible**
 Other image files available upon request.

Target Market(s)

New patient & Current Patients

Industry/Entity Type

Optometry

Contact Information for Business Card

High-tech optometry practice with 3 doctors seeking new business card.  We provide eye exams, sell, designer glasses/contacts/specialty eyewear and treat ocular diseases.  For our business cards, we are seeking fresh, clean, and crisp design as we grow our team (staffing change).  Simply adding doctors is making the card look busy/cluttered.  Looking for professional, less cluttered look yet still have our logo, doctor names, phone, address, and website....If possible!  :) Names: Marcia Trelford, O.D. Ned Pallister, O.D. Oona Ferrant, O.D. Phone: 555-014-2738 Website: www.BrightLensHub.example Address:  417 Garnet R. Holloway, Maple Hollow, NS 00000 Ultimately we have the main business card with all doctor sames and that card has two versions  (front is always the same).  The back has two designs (1) displays next appointment time/date, (2) for "general use" (non-appointment.)    I have attached what we have used in the past.   We also need a design template for each team member in our practice with their name, title, and email.   Those should be designed with the "general use" back (see attached). **Open to entirely new design so don't feel obligated to keep current format.  Need new perspective!  Also including our watermark and some other design features we have consistently used in past in our portfolio.  Included are two options for logos--vertical and horizontal. **I also would like to remove "Member of Sight Alliance" on our logo if possible**  Other image files available upon request.

Font styles to use
Other font styles liked:
• We have used Montserrat / Yellowtail in the past

Colors

Designer to choose colors to be used in the design.

Requirements
Must have
• Clean & Fresh Design with Logo / Info provided in description. Horizontal orientation. **I have included the CMYK colors we currently have in our logo.
Should not have
• Cluttered

```html
<!DOCTYPE html>
<html lang="en">
<head>
<meta charset="utf-8">
<title>Bright Lens Hub – Business Cards</title>
<link rel="stylesheet" href="https://fonts.googleapis.com/css2?family=Montserrat:wght@400;500&display=swap">
<style>
  :root {
    --page: #b0b0b0;
    --card: #262626;
    --white: #ffffff;
    --slate: #5d7e8e;
    --sky: #a6dcea;
    --gold: #e2b31f;
    --rule: #8a9aa2;
  }
  * { margin: 0; padding: 0; box-sizing: border-box; }
  html, body {
    width: 1081px; height: 1200px; overflow: hidden;
    background: var(--page);
    font-family: "Montserrat", sans-serif;
  }
  .canvas { position: relative; width: 1081px; height: 1200px; }
  .card {
    position: absolute; left: 90px; width: 900px; height: 515px;
    background: var(--card); border-radius: 46px; overflow: hidden;
    color: var(--white);
  }
  .card--front { top: 57px; }
  .card--back { top: 628px; }

  .brand-name {
    font-family: "Montserrat", sans-serif; font-weight: 400;
    color: var(--white); letter-spacing: 1px; white-space: nowrap;
  }
  .card--front .brand-name { position: absolute; left: 50px; top: 58px; font-size: 42px; }

  .doctors { position: absolute; left: 50px; top: 160px; font-weight: 500; font-size: 25px; line-height: 33px; }
  .doctor--slate { color: var(--slate); }
  .doctor--sky { color: var(--sky); }
  .doctor--gold { color: var(--gold); }

  .address { position: absolute; left: 50px; top: 282px; font-size: 21px; line-height: 28px; }

  .contacts { position: absolute; left: 50px; top: 366px; list-style: none; font-size: 21px; }
  .contacts li { display: flex; align-items: center; height: 35px; }
  .contacts svg { width: 18px; height: 18px; margin-right: 9px; flex: none; }

  .iris-mark {
    position: absolute; left: 530px; top: 70px; width: 380px; height: 380px;
    border-radius: 50%;
    background: radial-gradient(circle at 50% 50%, var(--sky) 0 48%, var(--slate) 49% 60%, var(--card) 61%);
  }

  .back-brand {
    position: absolute; left: 0; right: 0; top: 98px;
    display: flex; justify-content: center; align-items: center; gap: 26px;
  }
  .back-brand .dot { width: 58px; height: 58px; border-radius: 50%; background: var(--sky); }
  .back-brand .brand-name { font-size: 50px; }

  .appointment {
    position: absolute; left: 64px; top: 250px; width: 770px; height: 166px;
    background: var(--white); border-radius: 18px;
  }
  .appointment-row {
    position: absolute; left: 48px; right: 48px; display: flex; align-items: flex-end;
    color: var(--slate); font-weight: 500; font-size: 22px;
  }
  .appointment-row--date { top: 38px; }
  .appointment-row--time { top: 104px; }
  .appointment-row .label { width: 87px; flex: none; }
  .appointment-row .line { flex: 1; border-bottom: 1.5px solid var(--rule); margin-bottom: 4px; }

  .notice { position: absolute; left: 0; right: 0; top: 453px; text-align: center; font-size: 21px; }
</style>
</head>
<body>
<main class="canvas">

  <section class="card card--front" aria-label="Business card front">
    <div class="brand-name">brightlenshub</div>

    <div class="doctors">
      <p class="doctor doctor--slate">Marcia Trelford, O.D.</p>
      <p class="doctor doctor--sky">Ned Pallister, O.D.</p>
      <p class="doctor doctor--gold">Oona Ferrant, O.D.</p>
    </div>

    <p class="address">417 Garnet R. Holloway<br>Maple Hollow, NS 00000</p>

    <ul class="contacts">
      <li>
        <svg viewBox="0 0 20 20"><path d="M4 2l4 1 1 4-2 1.5a10 10 0 0 0 4.5 4.5L13 11l4 1 1 4-2 2C9 18 2 11 2 4z" fill="var(--gold)"/></svg>
        555-014-2738
      </li>
      <li>
        <svg viewBox="0 0 20 20"><rect x="2" y="5" width="16" height="11" fill="var(--gold)"/><path d="M2 5l8 6 8-6" fill="none" stroke="var(--card)" stroke-width="1.5"/></svg>
        info@BrightLensHub.example
      </li>
      <li>
        <svg viewBox="0 0 20 20" fill="none" stroke="var(--gold)" stroke-width="1.6"><circle cx="10" cy="10" r="7.5"/><ellipse cx="10" cy="10" rx="3.5" ry="7.5"/><path d="M2.5 10h15M4 6h12M4 14h12"/></svg>
        www.BrightLensHub.example
      </li>
    </ul>

    <div class="iris-mark" role="img" aria-label="Large decorative brand emblem area"></div>
  </section>

  <section class="card card--back" aria-label="Business card back, appointment version">
    <div class="back-brand">
      <span class="dot"></span>
      <span class="brand-name">brightlenshub</span>
    </div>

    <div class="appointment">
      <div class="appointment-row appointment-row--date"><span class="label">Date :</span><span class="line"></span></div>
      <div class="appointment-row appointment-row--time"><span class="label">Time :</span><span class="line"></span></div>
    </div>

    <p class="notice">If you are unable to keep your appointment kindly give us 24 hour notice</p>
  </section>

</main>
</body>
</html>
```